Business Card Design

I need a business card design for a new business based in Karrow Valley Region.
I specialize in residential window cleaning & general handyman maintenance.

Industry/Entity Type

Business

Contact Information for Business Card

Dale Marsh - 512 SILVER HAWK DETAILING
- Window Cleaning
- House Maintenance

```html
<!DOCTYPE html>
<html lang="en">
<head>
<meta charset="utf-8">
<title>Dale Marsh – Business Card</title>
<link href="https://fonts.googleapis.com/css2?family=Russo+One&family=Roboto:wght@400;500&family=Roboto+Condensed:wght@700&display=swap" rel="stylesheet">
<style>
  :root {
    --page-bg: #d9d6d2;
    --card-white: #f1f1f1;
    --brand-red: #dc1f26;
    --band-dark: #232323;
    --band-mid: #5a5a5a;
    --text-light: #ffffff;
  }
  * { margin: 0; padding: 0; box-sizing: border-box; }
  html, body {
    width: 1200px;
    height: 697px;
    overflow: hidden;
    background: var(--page-bg);
  }
  .card {
    position: absolute;
    left: 110px;
    top: 68px;
    width: 980px;
    height: 560px;
    background: var(--brand-red);
    overflow: hidden;
    box-shadow: 0 14px 30px rgba(0,0,0,0.25);
  }
  .card-top {
    position: absolute;
    left: 0; top: 0;
    width: 100%;
    height: 262px;
    background: var(--card-white);
  }
  .brand-name {
    position: absolute;
    left: 58px;
    top: 22px;
    font-family: "Russo One", sans-serif;
    font-size: 128px;
    line-height: 1;
    letter-spacing: 2px;
    color: var(--brand-red);
    white-space: nowrap;
  }
  .business-banner {
    position: absolute;
    left: 58px;
    top: 168px;
    height: 66px;
    padding: 0 22px;
    background: var(--brand-red);
    font-family: "Roboto", sans-serif;
    font-weight: 500;
    font-size: 52px;
    line-height: 66px;
    color: var(--text-light);
    white-space: nowrap;
  }
  .services-band {
    position: absolute;
    left: 0; top: 262px;
    width: 100%;
    height: 72px;
    background: linear-gradient(to bottom, var(--band-dark), var(--band-mid));
    display: flex;
    align-items: center;
    padding-left: 58px;
    font-family: "Roboto Condensed", sans-serif;
    font-weight: 700;
    font-size: 40px;
    color: var(--text-light);
    text-transform: uppercase;
    white-space: nowrap;
  }
  .service-divider {
    width: 2px;
    height: 42px;
    margin: 0 26px;
    background: rgba(255,255,255,0.35);
  }
  .contact-list {
    position: absolute;
    left: 58px;
    top: 362px;
    list-style: none;
    font-family: "Roboto", sans-serif;
    font-size: 32px;
    color: var(--text-light);
  }
  .contact-item {
    display: flex;
    align-items: center;
    height: 46px;
    white-space: nowrap;
  }
  .contact-icon {
    width: 28px;
    height: 28px;
    margin-right: 22px;
    fill: var(--text-light);
    flex: none;
  }
</style>
</head>
<body>
  <div class="card">
    <div class="card-top">
      <div class="brand-name">DALE MARSH</div>
      <div class="business-banner">512 SILVER HAWK DETAILING</div>
    </div>

    <div class="services-band">
      <span class="service">Window Cleaning</span>
      <span class="service-divider"></span>
      <span class="service">House Maintenance</span>
    </div>

    <ul class="contact-list">
      <li class="contact-item">
        <svg class="contact-icon" viewBox="0 0 28 28" aria-hidden="true">
          <path d="M2 6h24v16H2z M3 7l11 8 11-8" fill="none" stroke="#fff" stroke-width="2"/>
        </svg>
        hello@dalemarshdetailing.com
      </li>
      <li class="contact-item">
        <svg class="contact-icon" viewBox="0 0 28 28" aria-hidden="true">
          <path d="M4 10c0-4 5-6 10-6s10 2 10 6v2h-6v-3h-8v3H4z"/>
          <rect x="6" y="14" width="16" height="10" rx="2"/>
        </svg>
        555.201.3344
      </li>
      <li class="contact-item">
        <svg class="contact-icon" viewBox="0 0 28 28" aria-hidden="true">
          <g fill="none" stroke="#fff" stroke-width="2">
            <circle cx="14" cy="14" r="11"/>
            <ellipse cx="14" cy="14" rx="5" ry="11"/>
            <path d="M3 14h22M5 8h18M5 20h18"/>
          </g>
        </svg>
        www.dalemarshdetailing.com
      </li>
      <li class="contact-item">
        <svg class="contact-icon" viewBox="0 0 28 28" aria-hidden="true">
          <path d="M14 2a8 8 0 0 0-8 8c0 6 8 16 8 16s8-10 8-16a8 8 0 0 0-8-8zm0 11a3 3 0 1 1 0-6 3 3 0 0 1 0 6z"/>
        </svg>
        Karrow Valley Region
      </li>
    </ul>
  </div>
</body>
</html>
```